Cover Page Design

Create a new cover page in a sleek modern look that consists of our logo as provided. This cover page will be used in presentations and should only have colors featured in our branding efforts.

Target Market(s)

Architectural and Interior Design Clients

Industry/Entity Type

Interior Design

Font styles to use
Other font styles liked:
• see attached logo

Colors

Designer to choose colors to be used in the design.

Requirements
Must have
• Clean look, no pictures. just logo.
Nice to have
• colors that relate to our brand.
Should not have
• No colors not featured in our branding:
• www.velmacardwick.com

```html
<!DOCTYPE html>
<html lang="en">
<head>
<meta charset="utf-8">
<title>Velma Cardwick + Partners — Cover Pages</title>
<link rel="stylesheet" href="https://fonts.googleapis.com/css2?family=Jost:wght@400;500&display=swap">
<style>
  :root {
    --board-grey: #b0b1b3;
    --brand-blue: #0276c0;
    --brand-mist: #d6e8f5;
    --paper: #ffffff;
    --ink: #2a2a2a;
  }
  * { margin: 0; padding: 0; box-sizing: border-box; }
  html, body {
    width: 960px;
    height: 1200px;
    overflow: hidden;
    background: var(--board-grey);
    font-family: "Jost", "Helvetica Neue", Arial, sans-serif;
  }
  .board { position: relative; width: 960px; height: 1200px; }
  .cover {
    position: absolute;
    left: 96px;
    width: 768px;
    height: 432px;
    overflow: hidden;
  }
  .cover--light { top: 113px; }
  .cover--dark  { top: 654px; }
  .cover__field { position: absolute; inset: 0; display: block; }

  .brand { position: absolute; left: 0; top: 0; width: 768px; height: 432px; }
  .brand__dot {
    position: absolute;
    left: 456px; top: 185px;
    width: 56px; height: 56px;
    border-radius: 50%;
    background: var(--brand-blue);
  }
  .brand__name {
    position: absolute;
    left: 521px; top: 196px;
    width: 202px;
    font-size: 21px;
    font-weight: 400;
    line-height: 1;
    letter-spacing: 0.6px;
    white-space: nowrap;
    color: var(--ink);
  }
  .brand__partners {
    position: absolute;
    left: 521px; top: 220px;
    width: 202px;
    text-align: right;
    font-size: 8px;
    font-weight: 400;
    letter-spacing: 5px;
    margin-right: -5px;
    line-height: 1;
    color: var(--ink);
  }
  .brand__rule {
    position: absolute;
    left: 514px; top: 236px;
    width: 254px; height: 1.5px;
    background: linear-gradient(to right, rgba(2,118,192,0), var(--brand-blue) 45%);
  }
  .brand__tagline {
    position: absolute;
    left: 521px; top: 247px;
    font-size: 7.5px;
    font-weight: 500;
    letter-spacing: 2.05px;
    line-height: 1;
    white-space: nowrap;
    color: var(--ink);
  }

  .cover--dark .brand__dot { background: var(--paper); }
  .cover--dark .brand__name,
  .cover--dark .brand__partners,
  .cover--dark .brand__tagline { color: var(--paper); }
  .cover--dark .brand__rule {
    background: linear-gradient(to right, rgba(255,255,255,0), var(--paper) 45%);
  }
</style>
</head>
<body>
<main class="board">

  <section class="cover cover--light" aria-label="Cover page, light version">
    <svg class="cover__field" width="768" height="432" viewBox="0 0 768 432" aria-hidden="true">
      <rect width="768" height="432" fill="var(--paper)"/>
      <rect x="431" y="0" width="337" height="177" fill="var(--brand-mist)"/>
      <rect x="0" y="266" width="768" height="166" fill="var(--brand-mist)"/>
      <rect x="198" y="0" width="232" height="132" fill="var(--brand-blue)"/>
      <rect x="0" y="177" width="430" height="89" fill="var(--brand-blue)"/>
      <rect x="0" y="330" width="430" height="102" fill="var(--brand-blue)"/>
    </svg>
    <div class="brand">
      <span class="brand__dot"></span>
      <p class="brand__name">VELMA CARDWICK</p>
      <p class="brand__partners">+ PARTNERS</p>
      <span class="brand__rule"></span>
      <p class="brand__tagline">ARCHITECTURE | INTERIOR DESIGN</p>
    </div>
  </section>

  <section class="cover cover--dark" aria-label="Cover page, blue version">
    <svg class="cover__field" width="768" height="432" viewBox="0 0 768 432" aria-hidden="true">
      <rect width="768" height="432" fill="var(--brand-blue)"/>
      <rect x="431" y="0" width="337" height="177" fill="var(--brand-mist)"/>
      <rect x="0" y="266" width="768" height="166" fill="var(--brand-mist)"/>
      <rect x="198" y="0" width="232" height="132" fill="var(--paper)"/>
      <rect x="0" y="177" width="430" height="89" fill="var(--paper)"/>
      <rect x="0" y="330" width="430" height="102" fill="var(--paper)"/>
      <rect x="431" y="177" width="337" height="89" fill="var(--brand-blue)"/>
    </svg>
    <div class="brand">
      <span class="brand__dot"></span>
      <p class="brand__name">VELMA CARDWICK</p>
      <p class="brand__partners">+ PARTNERS</p>
      <span class="brand__rule"></span>
      <p class="brand__tagline">ARCHITECTURE | INTERIOR DESIGN</p>
    </div>
  </section>

</main>
</body>
</html>
```